Corvane Large Loss Tradeshow Booth Design

We need a tradeshow booth design for a 10x20 booth. We are a COMMERCIAL ONLY disaster restoration company focusing on water and flood restoration, fire and smoke remediation, mold and biohazard, structural repair and asset protection.

These are the links to the booth we need graphics designed for. The spec sheets for them are also in the attachments.
https://www.expostallden.com/Pelmora-Radial-Swift-Truss-p/pelmora.htm?CartID=2
https://www.expostallden.com/Tidecrest-39-Counter-p/tdc-39.htm?CartID=1
https://www.expostallden.com/6ft-Stretch-Table-Cover-p/tbl-6-stretch.htm?CartID=5

Target Market(s)

Real Estate, Educational Facilities, Hospitality Facilities, Medical Facilities

Industry/Entity Type

Construction

Requirements
Must have
• Our logo. The colors from the attached presentation. Pictures of COMMERCIAL ONLY facilities and losses (can use some from attached presentation). Our services (water and flood, fire and smoke, mold and biohazard, structural repair, asset protection). Our slogan (Exceeding your expectations when you need it most).
Nice to have
• Include the above
Should not have
• Do not include anything residential looking at all (no pictures). Do not include the case studies on the pictures.

```html
<!DOCTYPE html>
<html lang="en">
<head>
<meta charset="utf-8">
<title>Corvane Large Loss – Tradeshow Booth Graphics</title>
<link rel="stylesheet" href="https://fonts.googleapis.com/css2?family=Roboto:wght@700;900&family=Baloo+2:wght@800&display=swap">
<style>
  :root{
    --backdrop-light:#d0d1d3;
    --backdrop-dark:#6b6c6f;
    --board:#ffffff;
    --sky-light:#d4ecfb;
    --sky:#7cc4ef;
    --blue:#2a8fd6;
    --blue-deep:#1565b4;
    --orange:#f28c22;
    --orange-dark:#6a3a10;
    --copy-grey:#6e6e70;
    --haze:#e7e8e9;
    --water:#3a3b3b;
  }
  *{margin:0;padding:0;box-sizing:border-box}
  html,body{width:1200px;height:502px;overflow:hidden}
  body{
    position:relative;
    background:linear-gradient(var(--backdrop-light) 0 72%, var(--backdrop-dark) 72% 100%);
    font-family:"Roboto",Arial,sans-serif;
  }
  .booth-board{
    position:absolute;left:20px;top:54px;width:1160px;height:392px;
    background:var(--board);
    box-shadow:6px 8px 10px rgba(0,0,0,.35);
  }
  .panel{position:absolute;top:32px;height:344px;overflow:hidden}
  .panel svg{position:absolute;inset:0;width:100%;height:100%}
  .panel--end-left{left:32px;width:154px}
  .panel--narrow-a{left:204px;width:103px}
  .panel--wide-a{left:336px;width:173px}
  .panel--centre{left:538px;width:103px}
  .panel--wide-b{left:669px;width:173px}
  .panel--narrow-b{left:870px;width:104px}
  .panel--end-right{left:993px;width:153px}

  .brand{position:absolute;left:0;right:0;text-align:center;color:var(--orange);font-weight:900;line-height:1}
  .brand__name{display:block;letter-spacing:.5px}
  .brand__tag{display:block;border-top:1.5px solid var(--orange);border-bottom:1.5px solid var(--orange);margin:2px auto 0;padding:1px 0;font-weight:900}
  .brand--small{top:110px}
  .brand--small .brand__name{font-size:20px}
  .brand--small .brand__tag{font-size:7.5px;width:104px}
  .brand--large{top:92px}
  .brand--large .brand__name{font-size:30px}
  .brand--large .brand__tag{font-size:10px;width:140px}

  .services{position:absolute;left:0;right:0;list-style:none;text-align:center;color:var(--copy-grey);font-weight:700;text-transform:uppercase}
  .services--large{top:156px;font-size:11.4px;line-height:14px}
  .services--small{top:164px;font-size:7px;line-height:9.2px}

  .slogan{
    position:absolute;left:0;right:0;top:164px;text-align:center;
    font-family:"Baloo 2","Roboto",sans-serif;font-weight:800;font-size:14px;line-height:15.5px;
    color:var(--orange);text-transform:uppercase;
    -webkit-text-stroke:.6px var(--orange-dark);
  }
</style>
</head>
<body>
<div class="booth-board">

  <!-- End panel left -->
  <section class="panel panel--end-left">
    <svg viewBox="0 0 154 344" preserveAspectRatio="none">
      <defs>
        <linearGradient id="scene" x1="0" y1="0" x2="0" y2="1">
          <stop offset="0" stop-color="#eceded"/><stop offset=".55" stop-color="#d4d6d7"/>
          <stop offset=".68" stop-color="#6a6b6b"/><stop offset="1" stop-color="#2f3030"/>
        </linearGradient>
        <linearGradient id="sky" x1="0" y1="0" x2="0" y2="1">
          <stop offset="0" stop-color="#a9dcf8"/><stop offset="1" stop-color="#58b3ea"/>
        </linearGradient>
      </defs>
      <rect width="154" height="344" fill="url(#scene)" role="img" aria-label="Photo of a flooded commercial plaza with city towers"/>
      <path d="M0 0H154V78Q70 88 0 28Z" fill="url(#sky)"/>
      <path d="M0 28Q70 88 154 78" fill="none" stroke="#fff" stroke-width="5"/>
      <path d="M0 40Q70 96 154 86" fill="none" stroke="var(--blue)" stroke-width="5"/>
      <path d="M0 50Q70 104 154 94" fill="none" stroke="var(--blue-deep)" stroke-width="3"/>
      <path d="M0 330Q60 318 154 320V344H0Z" fill="var(--orange)"/>
    </svg>
    <div class="brand brand--small"><span class="brand__name">CORVANE</span><span class="brand__tag">RESTORATION SERVICES</span></div>
    <ul class="services services--large"><li>Water and Flood</li><li>Fire and Smoke</li><li>Mold and Biohazard</li><li>Structural Repair</li><li>Asset Protection</li></ul>
  </section>

  <!-- Narrow panel A -->
  <section class="panel panel--narrow-a">
    <svg viewBox="0 0 103 344" preserveAspectRatio="none">
      <rect width="103" height="344" fill="url(#scene)" role="img" aria-label="Photo of office towers over a flooded street"/>
      <path d="M0 0H103V52Q50 64 0 82Z" fill="url(#sky)"/>
      <path d="M0 82Q50 64 103 52" fill="none" stroke="var(--blue)" stroke-width="3"/>
      <path d="M0 328Q50 318 103 322V344H0Z" fill="var(--orange)"/>
    </svg>
    <ul class="services services--small"><li>Water and Flood</li><li>Fire and Smoke</li><li>Mold and Biohazard</li><li>Structural Repair</li><li>Asset Protection</li></ul>
  </section>

  <!-- Wide panel A -->
  <section class="panel panel--wide-a">
    <svg viewBox="0 0 173 344" preserveAspectRatio="none">
      <rect width="173" height="344" fill="url(#scene)" role="img" aria-label="Photo of a flooded commercial district"/>
      <path d="M0 0H173V14Q90 12 0 40Z" fill="url(#sky)"/>
      <path d="M0 40Q90 12 173 14" fill="none" stroke="#fff" stroke-width="4"/>
      <path d="M0 46Q90 20 173 22" fill="none" stroke="var(--blue)" stroke-width="5"/>
      <path d="M0 54Q90 30 173 30" fill="none" stroke="var(--blue-deep)" stroke-width="3"/>
      <path d="M0 322Q90 316 173 318V344H0Z" fill="var(--orange)"/>
    </svg>
    <div class="brand brand--large"><span class="brand__name">CORVANE</span><span class="brand__tag">RESTORATION SERVICES</span></div>
    <p class="slogan">Exceeding your<br>expectations when<br>you need it most</p>
  </section>

  <!-- Centre panel -->
  <section class="panel panel--centre">
    <svg viewBox="0 0 103 344" preserveAspectRatio="none">
      <rect width="103" height="344" fill="url(#scene)" role="img" aria-label="Photo of a flooded plaza with trees"/>
      <path d="M0 0H103V6L51.5 18 0 6Z" fill="url(#sky)"/>
      <path d="M0 10L51.5 22 103 10" fill="none" stroke="var(--blue)" stroke-width="5"/>
      <path d="M0 22L51.5 38 103 22V42L51.5 56 0 42Z" fill="var(--blue)"/>
      <path d="M0 44L51.5 58 103 44V64L51.5 94 0 64Z" fill="var(--blue-deep)"/>
      <path d="M0 318H103V344H0Z" fill="var(--orange)"/>
    </svg>
    <ul class="services services--small"><li>Water and Flood</li><li>Fire and Smoke</li><li>Mold and Biohazard</li><li>Structural Repair</li><li>Asset Protection</li></ul>
  </section>

  <!-- Wide panel B -->
  <section class="panel panel--wide-b">
    <svg viewBox="0 0 173 344" preserveAspectRatio="none">
      <rect width="173" height="344" fill="url(#scene)" role="img" aria-label="Photo of a flooded commercial district"/>
      <path d="M0 0H173V40Q90 12 0 14Z" fill="url(#sky)"/>
      <path d="M0 14Q90 12 173 40" fill="none" stroke="#fff" stroke-width="4"/>
      <path d="M0 22Q90 20 173 46" fill="none" stroke="var(--blue)" stroke-width="5"/>
      <path d="M0 30Q90 30 173 54" fill="none" stroke="var(--blue-deep)" stroke-width="3"/>
      <path d="M0 318Q90 316 173 322V344H0Z" fill="var(--orange)"/>
    </svg>
    <div class="brand brand--large"><span class="brand__name">CORVANE</span><span class="brand__tag">RESTORATION SERVICES</span></div>
    <p class="slogan">Exceeding your<br>expectations when<br>you need it most</p>
  </section>

  <!-- Narrow panel B -->
  <section class="panel panel--narrow-b">
    <svg viewBox="0 0 104 344" preserveAspectRatio="none">
      <rect width="104" height="344" fill="url(#scene)" role="img" aria-label="Photo of office towers over a flooded street"/>
      <path d="M0 0H104V82Q50 64 0 52Z" fill="url(#sky)"/>
      <path d="M0 52Q50 64 104 82" fill="none" stroke="var(--blue)" stroke-width="3"/>
      <path d="M0 322Q50 318 104 328V344H0Z" fill="var(--orange)"/>
    </svg>
    <ul class="services services--small"><li>Water and Flood</li><li>Fire and Smoke</li><li>Mold and Biohazard</li><li>Structural Repair</li><li>Asset Protection</li></ul>
  </section>

  <!-- End panel right -->
  <section class="panel panel--end-right">
    <svg viewBox="0 0 153 344" preserveAspectRatio="none">
      <rect width="153" height="344" fill="url(#scene)" role="img" aria-label="Photo of a flooded commercial plaza with city towers"/>
      <path d="M0 0H153V28Q84 88 0 78Z" fill="url(#sky)"/>
      <path d="M0 78Q84 88 153 28" fill="none" stroke="#fff" stroke-width="5"/>
      <path d="M0 86Q84 96 153 40" fill="none" stroke="var(--blue)" stroke-width="5"/>
      <path d="M0 94Q84 104 153 50" fill="none" stroke="var(--blue-deep)" stroke-width="3"/>
      <path d="M0 320Q94 318 153 330V344H0Z" fill="var(--orange)"/>
    </svg>
    <div class="brand brand--small"><span class="brand__name">CORVANE</span><span class="brand__tag">RESTORATION SERVICES</span></div>
    <ul class="services services--large"><li>Water and Flood</li><li>Fire and Smoke</li><li>Mold and Biohazard</li><li>Structural Repair</li><li>Asset Protection</li></ul>
  </section>

</div>
</body>
</html>
```